Kick Ass, Edgy, Fun, E commerce Embroidery Company Business Card

Sleek and edgy business card layout. main logo on front with business description (Custom Embroidery, the file is submitted is supposed to look like stitching)
Name, address, phone numbers, social icons (Facebook and Instagram) on back. The card will be black plastic and the front main logo will be printed Spot UV.

Target Market(s)

Small Business Owners

Contact Information for Business Card

Focused, not cluttered and sleek. Modern looking.

Font styles to use
Other font styles liked:
• Very clean and elegant

Colors
acd136

Requirements
Must have
• Custom Embroidery

our Tagline: Every Logo Has A Story - Thread Yours
Nice to have
• Social Icons for Facebook and Instagram
Should not have
• Too much visual noise

```html
<!DOCTYPE html>
<html lang="en">
<head>
<meta charset="utf-8">
<title>Kestrel Thread – Business Card</title>
<link href="https://fonts.googleapis.com/css2?family=Archivo+Black&family=Montserrat:wght@300;400;600;800&display=swap" rel="stylesheet">
<style>
  :root {
    --bg: #161617;
    --card: #3b3c3e;
    --lime: #acd136;
    --ink: #2e2f31;
    --white: #f2f2f2;
    --muted: #e4e4e4;
  }
  * { box-sizing: border-box; margin: 0; padding: 0; }
  html, body { width: 1200px; height: 1000px; overflow: hidden; }
  body {
    background: var(--bg);
    font-family: "Montserrat", sans-serif;
    position: relative;
  }
  .card {
    position: absolute;
    top: 150px;
    width: 400px;
    height: 700px;
    background: var(--card);
    border-radius: 22px;
    overflow: hidden;
  }
  .card--front { left: 150px; }
  .card--back { left: 650px; }

  /* Front */
  .brand {
    position: absolute;
    top: 130px;
    left: 0; right: 0;
    display: flex;
    flex-direction: column;
    align-items: center;
    gap: 34px;
  }
  .brand__dot {
    width: 110px; height: 110px;
    border-radius: 50%;
    background: var(--lime);
  }
  .brand__name {
    font-family: "Archivo Black", sans-serif;
    color: var(--white);
    font-size: 58px;
    line-height: 0.92;
    text-align: center;
    letter-spacing: 1px;
  }
  .band {
    position: absolute;
    left: 0; right: 0;
    top: 520px;
    height: 140px;
    background: var(--lime);
    display: flex;
    flex-direction: column;
    justify-content: center;
    align-items: center;
  }
  .band__service {
    font-weight: 800;
    color: var(--ink);
    font-size: 40px;
    line-height: 1.05;
    text-align: center;
    letter-spacing: 1px;
  }

  /* Back */
  .contact {
    position: absolute;
    top: 60px;
    left: 44px;
    right: 30px;
  }
  .contact__person {
    color: var(--lime);
    font-weight: 600;
    font-size: 20px;
    letter-spacing: 1px;
    margin-bottom: 38px;
  }
  .contact__company {
    color: var(--lime);
    font-weight: 600;
    font-size: 20px;
    letter-spacing: 1px;
    margin-bottom: 8px;
  }
  .contact__address {
    color: var(--muted);
    font-weight: 300;
    font-size: 19px;
    line-height: 1.4;
    margin-bottom: 28px;
  }
  .contact__list { list-style: none; }
  .contact__item {
    display: flex;
    align-items: center;
    gap: 14px;
    color: var(--muted);
    font-weight: 300;
    font-size: 19px;
    margin-bottom: 16px;
  }
  .contact__icon { width: 26px; height: 26px; flex: none; }
  .social {
    position: absolute;
    top: 432px;
    right: 40px;
    display: flex;
    gap: 22px;
  }
  .social__badge {
    width: 58px; height: 58px;
    border-radius: 50%;
    background: var(--lime);
  }
  .band__tagline {
    font-weight: 800;
    color: var(--white);
    font-size: 25px;
    letter-spacing: 1px;
    text-align: center;
  }
  .band__tagline-end {
    font-weight: 800;
    color: var(--ink);
    font-size: 22px;
    letter-spacing: 1px;
    margin-top: 10px;
  }
</style>
</head>
<body>

<section class="card card--front" aria-label="Business card front">
  <div class="brand">
    <div class="brand__dot"></div>
    <div class="brand__name">KESTREL<br>THREAD</div>
  </div>
  <div class="band">
    <p class="band__service">CUSTOM<br>EMBROIDERY</p>
  </div>
</section>

<section class="card card--back" aria-label="Business card back">
  <div class="contact">
    <p class="contact__person">DALTON REYES</p>
    <p class="contact__company">KESTREL THREAD INC</p>
    <p class="contact__address">4410 Granite Ridge Dr Ste 7<br>Lakewood, CO 80226</p>
    <ul class="contact__list">
      <li class="contact__item">
        <svg class="contact__icon" viewBox="0 0 26 26" aria-hidden="true">
          <circle cx="13" cy="13" r="12" fill="none" stroke="#acd136" stroke-width="1.5"/>
          <path d="M9 7.5l2.2 0.2 1 2.7-1.4 1.1a7 7 0 0 0 3.7 3.7l1.1-1.4 2.7 1 .2 2.2c-.3.9-1.2 1.5-2.2 1.5A10 10 0 0 1 7.5 9.7C7.5 8.7 8.1 7.8 9 7.5z" fill="#acd136"/>
        </svg>
        800 - 555 - 0147
      </li>
      <li class="contact__item">
        <svg class="contact__icon" viewBox="0 0 26 26" aria-hidden="true">
          <circle cx="13" cy="13" r="12" fill="none" stroke="#acd136" stroke-width="1.5"/>
          <rect x="7" y="8.5" width="12" height="9" rx="1" fill="none" stroke="#acd136" stroke-width="1.5"/>
          <path d="M7.5 9.5l5.5 4.2 5.5-4.2" fill="none" stroke="#acd136" stroke-width="1.5"/>
        </svg>
        info@kestrelthread.com
      </li>
      <li class="contact__item">
        <svg class="contact__icon" viewBox="0 0 26 26" aria-hidden="true">
          <circle cx="13" cy="13" r="12" fill="none" stroke="#acd136" stroke-width="1.5"/>
          <circle cx="13" cy="13" r="6.5" fill="none" stroke="#acd136" stroke-width="1.3"/>
          <path d="M6.5 13h13M13 6.5c-2.5 3.5-2.5 9.5 0 13M13 6.5c2.5 3.5 2.5 9.5 0 13" fill="none" stroke="#acd136" stroke-width="1.3"/>
        </svg>
        www.KestrelThread.com
      </li>
      <li class="contact__item">
        <svg class="contact__icon" viewBox="0 0 26 26" aria-hidden="true">
          <circle cx="13" cy="13" r="12" fill="none" stroke="#acd136" stroke-width="1.5"/>
          <circle cx="13" cy="13" r="6.5" fill="none" stroke="#acd136" stroke-width="1.3"/>
          <path d="M6.5 13h13M13 6.5c-2.5 3.5-2.5 9.5 0 13M13 6.5c2.5 3.5 2.5 9.5 0 13" fill="none" stroke="#acd136" stroke-width="1.3"/>
        </svg>
        www.kestrelthread.com
      </li>
    </ul>
  </div>
  <div class="social">
    <div class="social__badge" role="img" aria-label="Photo sharing profile"></div>
    <div class="social__badge" role="img" aria-label="Social network profile"></div>
  </div>
  <div class="band">
    <p class="band__tagline">EVERY LOGO HAS A STORY</p>
    <p class="band__tagline-end">THREAD YOURS</p>
  </div>
</section>

</body>
</html>
```